Business Card Design for Cybersecurity Company - Quorvent Systems

We need a business card design for our new cybersecurity company, Quorvent. We’re going for a clean, hi tech look that feels modern, premium, and trustworthy. We want a design that really stands out and makes people say WOW when we hand it over!

Quorvent delivers reliable IT support and managed services for small and mid sized businesses. We help companies stay secure, efficient, and connected through proactive monitoring, cybersecurity services, cloud management, and remote support.

Target Market(s)

Designers should target small and mid sized businesses that need dependable cybersecurity and IT support.

Industry/Entity Type

Cybersecurity, Managed Service Provider, IT services

Contact Information for Business Card

Contact information

Requirements
Must have
• The card should look clean, modern, and tech focused, with the Quorvent logo, clear contact info, and strong readability. It needs to feel premium and professional while still keeping a simple layout that fits a cybersecurity and IT brand.
Nice to have
• Nice to have elements include subtle touches that give the card a modern, tech feel, along with a layout that works well in different background styles.
Should not have
• The card should avoid clutter, loud graphics, or anything that takes attention away from the logo and contact details.

```html
<!DOCTYPE html>
<html lang="en">
<head>
<meta charset="utf-8">
<title>Quorvent Systems – Business Card</title>
<link href="https://fonts.googleapis.com/css2?family=Montserrat:wght@400;500;700;800&display=swap" rel="stylesheet">
<style>
  :root {
    --backdrop: #2a2a2c;
    --card: #151516;
    --white: #f4f4f6;
    --text: #e6e6ea;
    --violet: #6a52c9;
    --blue: #4a7fe0;
    --icon: #7d6ae0;
  }
  * { margin: 0; padding: 0; box-sizing: border-box; }
  html, body {
    width: 1200px; height: 874px; overflow: hidden;
    background: var(--backdrop);
    font-family: "Montserrat", sans-serif;
  }
  .canvas { position: relative; width: 1200px; height: 874px; }
  .card {
    position: absolute; left: 290px;
    width: 620px; height: 354px;
    background: var(--card);
    border-radius: 22px;
    box-shadow: 0 12px 30px rgba(0,0,0,.45);
    overflow: hidden;
  }
  .card--front { top: 43px; }
  .card--back { top: 477px; }

  .wordmark { display: flex; align-items: center; gap: 16px; }
  .wordmark__square { width: 34px; height: 34px; background: var(--violet); flex: none; }
  .wordmark__name { color: var(--white); font-weight: 700; letter-spacing: .5px; white-space: nowrap; }

  .card--front .wordmark {
    position: absolute; left: 0; right: 0; top: 0; bottom: 0;
    justify-content: center;
  }
  .card--front .wordmark__name { font-size: 44px; }

  .card--back .wordmark { position: absolute; left: 44px; top: 156px; gap: 10px; }
  .card--back .wordmark__square { width: 20px; height: 20px; }
  .card--back .wordmark__name { font-size: 22px; }

  .divider {
    position: absolute; left: 318px; top: 58px; width: 2px; height: 238px;
    background: linear-gradient(to bottom, var(--violet), var(--blue));
  }
  .contact { position: absolute; left: 340px; top: 58px; color: var(--text); }
  .contact__name { font-size: 27px; font-weight: 800; color: var(--violet); line-height: 1.1; margin-bottom: 8px; }
  .contact__line { font-size: 14.5px; font-weight: 500; line-height: 1.45; }
  .contact__block { margin-bottom: 10px; }
  .contact__list { list-style: none; }
  .contact__item { display: flex; align-items: center; gap: 9px; font-size: 14.5px; font-weight: 500; line-height: 1.5; }
  .contact__item svg { width: 14px; height: 14px; fill: var(--icon); flex: none; }
</style>
</head>
<body>
<main class="canvas">
  <section class="card card--front" aria-label="Card front">
    <div class="wordmark">
      <span class="wordmark__square"></span>
      <span class="wordmark__name">Quorvent Systems</span>
    </div>
  </section>

  <section class="card card--back" aria-label="Card back">
    <div class="wordmark">
      <span class="wordmark__square"></span>
      <span class="wordmark__name">Quorvent Systems</span>
    </div>
    <div class="divider"></div>
    <div class="contact">
      <h1 class="contact__name">Daniel Marsh</h1>
      <div class="contact__block">
        <p class="contact__line">Owner | CEO</p>
        <p class="contact__line">Quorvent Systems</p>
      </div>
      <div class="contact__block">
        <p class="contact__line">PO Box 51820,</p>
        <p class="contact__line">Orlando, FL 32801</p>
      </div>
      <ul class="contact__list">
        <li class="contact__item">
          <svg viewBox="0 0 24 24"><path d="M6.6 10.8a15.1 15.1 0 0 0 6.6 6.6l2.2-2.2a1 1 0 0 1 1-.25 11.4 11.4 0 0 0 3.6.57 1 1 0 0 1 1 1V20a1 1 0 0 1-1 1A17 17 0 0 1 3 4a1 1 0 0 1 1-1h3.5a1 1 0 0 1 1 1c0 1.25.2 2.45.57 3.57a1 1 0 0 1-.25 1z"/></svg>
          (855) 410-QRVT
        </li>
        <li class="contact__item">
          <svg viewBox="0 0 24 24"><path d="M7 1h10a2 2 0 0 1 2 2v18a2 2 0 0 1-2 2H7a2 2 0 0 1-2-2V3a2 2 0 0 1 2-2zm0 3v14h10V4zm5 15.2a1.2 1.2 0 1 0 0 2.4 1.2 1.2 0 0 0 0-2.4z"/></svg>
          (407) 555-0182
        </li>
        <li class="contact__item">
          <svg viewBox="0 0 24 24"><path d="M2 5h20v14H2zm2 2v.5l8 5 8-5V7l-8 5z"/></svg>
          daniel@quorvent.com
        </li>
        <li class="contact__item">
          <svg viewBox="0 0 24 24"><path d="M12 2a10 10 0 1 0 0 20 10 10 0 0 0 0-20zm-1 17.9A8 8 0 0 1 4.1 11H7c.1 3.2 1.5 6.3 4 8.9zM4.1 9A8 8 0 0 1 11 4.1C8.6 6.7 7.2 9.8 7 13zm8.9 10.9c2.5-2.6 3.9-5.7 4-8.9h2.9a8 8 0 0 1-6.9 8.9zM17 9c-.1-3.2-1.5-6.3-4-8.9A8 8 0 0 1 19.9 9z"/></svg>
          quorvent.com
        </li>
      </ul>
    </div>
  </section>
</main>
</body>
</html>
```